BrightPlacely.com Wordpress Theme

Hi,

I am looking for a new theme for my wordpress site. The site looks average at the moment and needs a boost. I want to have a better user experience for publishers and advertisers and the proposition for each needs to be clear with better links to registration for both.

Publisher and Advertiser sign up buttons should be on the home page.

I am leaving the brief open save I request that you use green colours on the template.

I want room to be able to add more tabs on the top level if we introduce a blog or other services.

The layout needs to be solid and please work with the copy that's already there.

see http://brightplacely.example

I am looking forward to reviewing your ideas and designs.
Updates

The button to carbon neutral cert I am going to want to make smaller and put it in the bottom of the site.

Do not go down the too fluffy green route with windmills and fuzzy clouds. I am looking for something simple, professional but also organic with a bit of zest to it. 

We are not a niche player serving ads to green only site with green only ads. We simply neutralise the effect of online advertising campaigns.

Some decent images in the header on rotation could work I am not sure. I think these would have to be abstract and largely if not totally green in colour.

Target Market(s)

BrightPlacely.com is an online ad network. Our targets are publishers and advertisers. We bring them together through providing ad serving to the network we have built on behalf of our advertisers.

Advertisers are agencys, brands, large companies looking to sell online or create awareness of the brand.

Requirements
Must have
• Please keep the site clean and use green and white
• Call to action to both publishers and advertisers to join (buttons on home page)

```html
<!DOCTYPE html>
<html lang="en">
<head>
<meta charset="utf-8">
<title>BrightPlacely.com — Home</title>
<link href="https://fonts.googleapis.com/css2?family=Arimo:wght@400;700&display=swap" rel="stylesheet">
<style>
:root{
  --sky-top:#5fbfd3;
  --sky-bottom:#eef8f9;
  --leaf-dark:#1f6b2c;
  --leaf:#6a9e3a;
  --leaf-light:#b5cf45;
  --lime:#d4e05a;
  --nav:#857b6d;
  --nav-dark:#6e6558;
  --tab:#b5cf45;
  --band:#e6e4e0;
  --page:#f7f6f3;
  --text:#4a4a4a;
  --muted:#666;
  --heading-green:#6a9e3a;
  --button:#3f6f1f;
  --button-text:#f0f04a;
  --footer:#7aa336;
  --footer-top:#8fb846;
  --footer-line:#a7c66a;
  --bottom:#26271c;
}
*{margin:0;padding:0;box-sizing:border-box}
html,body{width:960px;height:1200px;overflow:hidden}
body{font-family:"Arimo",Arial,sans-serif;background:var(--page);color:var(--text);position:relative}
a{color:inherit;text-decoration:none}

.site-header{position:absolute;left:0;top:0;width:960px;height:160px;background:linear-gradient(var(--sky-top),var(--sky-bottom) 75%);overflow:hidden}
.header-landscape{position:absolute;left:0;bottom:0;width:960px;height:58px;background:linear-gradient(#d6e27a,#a9c845 45%,#6a9e3a)}
.brand{position:absolute;left:136px;top:26px;font-size:38px;font-weight:700;color:var(--leaf-dark);letter-spacing:-1px}
.tagline{position:absolute;left:147px;top:69px;font-size:18px;color:var(--leaf-dark);letter-spacing:-.5px}

.main-nav{position:absolute;left:0;top:160px;width:960px;height:40px;background:linear-gradient(var(--nav),var(--nav-dark));border-top:1px solid #9a907f}
.main-nav ul{list-style:none;display:flex;margin-left:136px;height:40px}
.main-nav li a{display:block;height:40px;line-height:40px;padding:0 10px;color:#fff;font-size:14.5px}
.main-nav li.current a{background:var(--tab);font-weight:700;padding:0 11px;border-left:1px solid #e0ea9a}
.sub-band{position:absolute;left:0;top:200px;width:960px;height:32px;background:linear-gradient(#dad7d2,var(--band) 40%,#eceae7);border-bottom:1px solid #dcdad5}

.intro{position:absolute;left:136px;top:268px;width:426px}
.intro .kicker{font-size:24px;color:var(--heading-green);letter-spacing:-1px;line-height:1}
.intro h1{font-size:37px;color:var(--heading-green);letter-spacing:-1.2px;line-height:1;font-weight:700}
.intro p{font-size:14.4px;line-height:19.2px;margin-top:6px;color:var(--text)}
.why{position:absolute;left:136px;top:468px;width:424px}
.why h2{font-size:19px;color:var(--heading-green);letter-spacing:-.5px}
.reason{display:flex;padding:11px 0 12px;border-bottom:1px solid #dcdad5;font-size:11.2px;line-height:16.8px;color:var(--muted)}
.reason:last-child{border:none}
.reason .num{width:27px;flex:none;font-size:24px;font-weight:700;color:#555;line-height:1.1}
.reason ul{list-style:none}
.reason b{color:#555}

.cta{position:absolute;left:608px;width:216px;height:142px;background:#fff;box-shadow:0 1px 3px rgba(0,0,0,.25);padding:6px}
.cta .inner{background:var(--leaf);height:130px;padding:16px 26px}
.cta .ask{color:#fff;font-size:14px;line-height:1;letter-spacing:-.5px}
.cta .role{color:#fff;font-size:21px;font-weight:700;letter-spacing:-.5px;line-height:1}
.cta .btn{display:block;margin-top:7px;width:152px;height:52px;line-height:52px;text-align:center;background:linear-gradient(var(--button),#34601a);color:var(--button-text);font-size:19px;letter-spacing:-.5px}
.badge{position:absolute;left:608px;top:603px;width:216px;height:107px;background:var(--leaf);padding:6px;box-shadow:0 1px 3px rgba(0,0,0,.25)}
.badge div{width:100%;height:100%;background:#fff}

.site-footer{position:absolute;left:0;top:846px;width:960px;height:314px;background:var(--footer)}
.footer-bar{height:40px;background:linear-gradient(var(--footer-top),#78a234);border-bottom:1px solid #c1d88a;display:flex}
.footer-bar h3{font-size:19px;color:#1f3a10;line-height:40px;letter-spacing:-.5px}
.footer-bar h3:nth-child(1){margin-left:137px;width:224px;border-right:1px solid #aac873}
.footer-bar h3:nth-child(2){padding-left:16px;width:240px;border-right:1px solid #aac873}
.footer-bar h3:nth-child(3){padding-left:16px}
.foot-col{position:absolute;top:50px;font-size:12px;color:#fff}
.foot-col ul{list-style:none}
.foot-col li{height:20.8px;line-height:20.5px;border-bottom:1px solid var(--footer-line)}
.foot-col li:last-child{border:none}
.col-pages{left:135px;width:209px}
.col-publishers{left:376px;width:212px;font-size:11.6px;line-height:16.8px;top:53px}
.col-info{left:615px;width:209px}

.bottom-bar{position:absolute;left:0;top:1160px;width:960px;height:40px;background:var(--bottom);display:flex;align-items:center}
.bottom-bar .foot-brand{margin-left:136px;font-size:18px;font-weight:700;color:var(--leaf-light);letter-spacing:-.5px}
.bottom-bar small{margin-left:20px;font-size:11px;color:#ddd;letter-spacing:-.3px}
</style>
</head>
<body>

<header class="site-header">
  <div class="header-landscape" role="img" aria-label="Rolling green hills landscape banner"></div>
  <a class="brand" href="http://brightplacely.example">BrightPlacely.com</a>
  <div class="tagline">Your ads, carbon free</div>
</header>

<nav class="main-nav">
  <ul>
    <li class="current"><a href="#">Home</a></li>
    <li><a href="#">Advertisers</a></li>
    <li><a href="#">Publishers</a></li>
    <li><a href="#">Referral</a></li>
    <li><a href="#">Offsetting</a></li>
    <li><a href="#">Contact</a></li>
  </ul>
</nav>
<div class="sub-band"></div>

<section class="intro">
  <div class="kicker">WELCOME TO</div>
  <h1>BRIGHTPLACELY</h1>
  <p><b>BrightPlacely.com</b> is a contextual advertising network and ad exchange that brings together publishers of high quality content with advertisers, enabling them to reach their target market whilst publishers monetize their sites through advertising that's in keeping with their sites.</p>
</section>

<section class="why">
  <h2>WHY SHOULD YOU CHOOSE US?</h2>
  <div class="reason">
    <span class="num">1</span>
    <ul>
      <li>- Hundreds of millions of monthly ad impressions across ours and our partner networks</li>
      <li>- 170+ content channels to target</li>
      <li>- B2B &amp; B2C traffic</li>
      <li>- Geo Targeting</li>
      <li>- Behavioural Targeting</li>
      <li>- Re-Targeting</li>
      <li>- Real Time Campaign Tracking &amp; Reporting</li>
      <li>- ROI tracking</li>
    </ul>
  </div>
  <div class="reason">
    <span class="num">2</span>
    <p>BrightPlacely.com collates high quality content across a range of specialist and generalist websites and blogs and equips advertisers with the tools to target visitors and optimize campaign performance.</p>
  </div>
  <div class="reason">
    <span class="num">3</span>
    <p>As you may have guested by our name <b>BrightPlacely.com</b> is both responsible and ethical.100% of the ads we serve are carbon offset meaning that you can feel good in the fact that the environmental impact of your advertising campaign has been neutralized.</p>
  </div>
</section>

<aside>
  <div class="cta" style="top:272px">
    <div class="inner">
      <div class="ask">ARE YOU AN</div>
      <div class="role">ADVERTISER?</div>
      <a class="btn" href="#">KNOW MORE</a>
    </div>
  </div>
  <div class="cta" style="top:434px">
    <div class="inner">
      <div class="ask">ARE YOU A</div>
      <div class="role">PUBLISHER?</div>
      <a class="btn" href="#">KNOW MORE</a>
    </div>
  </div>
  <div class="badge" role="img" aria-label="Carbon neutral website certificate badge"><div></div></div>
</aside>

<footer class="site-footer">
  <div class="footer-bar">
    <h3>Pages</h3>
    <h3>Publishers</h3>
    <h3>Useful Info</h3>
  </div>
  <div class="foot-col col-pages">
    <ul>
      <li><a href="#">Contact</a></li>
      <li><a href="#">Offsetting</a></li>
      <li><a href="#">Referral</a></li>
      <li><a href="#">Publishers</a></li>
      <li><a href="#">Ad Formats</a></li>
      <li><a href="#">Publisher Registration</a></li>
      <li><a href="#">Publisher Agreement</a></li>
      <li><a href="#">Advertisers</a></li>
      <li><a href="#">Ad Formats</a></li>
      <li><a href="#">Testimonials</a></li>
      <li><a href="#">Advertiser Registration</a></li>
      <li><a href="#">Advertiser Agreement</a></li>
    </ul>
  </div>
  <p class="foot-col col-publishers"><b>BrightPlacely.com</b> offers publishers to the opportunity to earn more income through text (inline text links) or by displaying targeted contextual advertising banner ads on their websites or blogs.</p>
  <div class="foot-col col-info">
    <ul>
      <li><a href="#">Contact Us</a></li>
      <li><a href="#">Terms &amp; Conditions : Advertisers</a></li>
      <li><a href="#">Terms &amp; Conditions : Publishers</a></li>
      <li><a href="#">User Guide: Advertisers</a></li>
      <li><a href="#">User Guide: Publishers</a></li>
    </ul>
  </div>
</footer>

<div class="bottom-bar">
  <span class="foot-brand">BrightPlacely.com</span>
  <small>Copyright BrightPlacely.com Ltd 2010</small>
</div>

</body>
</html>
```